Granite, Brass and Shingle Roofing LLC needs a new business card

I need a new business card because I have a new address.
I do slate copper and tile roofs. My webpage is: www.granitebrassandshingleroofing.com

```html
<!DOCTYPE html>
<html lang="en">
<head>
<meta charset="utf-8">
<title>Granite, Brass &amp; Shingle Roofing – Business Card</title>
<link href="https://fonts.googleapis.com/css2?family=Playfair+Display:wght@400;700;900&family=Arimo:wght@400&display=swap" rel="stylesheet">
<style>
  :root {
    --backdrop: #a9a9a9;
    --ink: #000000;
    --sky-blue: #519fcf;
    --paper: #ffffff;
    --rule: #2b4a63;
  }
  * { box-sizing: border-box; margin: 0; padding: 0; }
  html, body { width: 1200px; height: 1200px; overflow: hidden; }
  body {
    background: var(--backdrop);
    position: relative;
    font-family: "Arimo", Arial, sans-serif;
    color: var(--ink);
  }
  .card {
    position: absolute;
    top: 303px;
    width: 368px;
    height: 593px;
    overflow: hidden;
  }
  .card--front { left: 201px; background: var(--sky-blue); }
  .card--back  { left: 599px; background: var(--sky-blue); }

  /* front */
  .front-art {
    position: absolute;
    left: 0; top: 0;
    width: 100%;
    height: 455px;
    background: linear-gradient(160deg, var(--ink) 0%, var(--ink) 38%, var(--sky-blue) 72%);
  }
  .front-name {
    position: absolute;
    left: 47px;
    top: 472px;
    font-family: "Playfair Display", Georgia, serif;
    font-weight: 400;
    color: var(--ink);
    line-height: 1.05;
  }
  .front-name .line-top { display: block; font-size: 26px; }
  .front-name .line-main {
    display: block;
    font-size: 38px;
    font-weight: 700;
    letter-spacing: 4px;
    line-height: 1;
  }

  /* back */
  .back-top {
    position: absolute;
    left: 0; top: 0;
    width: 100%;
    height: 306px;
    background: var(--paper);
    display: flex;
    align-items: center;
    justify-content: center;
  }
  .back-name {
    font-family: "Playfair Display", Georgia, serif;
    font-weight: 400;
    color: var(--ink);
    line-height: 1.05;
    display: flex;
    align-items: center;
    gap: 10px;
  }
  .back-name .mark {
    width: 14px; height: 14px;
    background: var(--sky-blue);
    flex: none;
  }
  .back-name .line-top { display: block; font-size: 19px; }
  .back-name .line-main {
    display: block;
    font-size: 27px;
    font-weight: 700;
    letter-spacing: 3px;
    line-height: 1;
  }

  .contact {
    position: absolute;
    left: 0; right: 0;
    top: 338px;
    text-align: center;
  }
  .person {
    font-family: "Playfair Display", Georgia, serif;
    font-weight: 900;
    font-size: 20px;
    letter-spacing: 0.3px;
  }
  .role { font-size: 15px; margin-top: 1px; }
  .icon-row {
    display: flex;
    align-items: center;
    justify-content: center;
    gap: 4px;
    margin-top: 11px;
  }
  .icon-row .rule { width: 52px; height: 1px; background: var(--rule); margin: 0 1px; }
  .icon {
    width: 25px; height: 25px;
    background: var(--ink);
    border-radius: 4px;
    display: flex; align-items: center; justify-content: center;
  }
  .details { margin-top: 8px; font-size: 15.5px; line-height: 21.5px; }
  .details .web { font-size: 14.5px; white-space: nowrap; }
  .divider { width: 195px; height: 1px; background: var(--rule); margin: 11px auto 0; }
  .address { margin-top: 14px; font-size: 15.5px; line-height: 21.5px; }
</style>
</head>
<body>

<section class="card card--front">
  <div class="front-art" role="img" aria-label="Large roof illustration with chimney and a roofer working on the ridge"></div>
  <h1 class="front-name">
    <span class="line-top">Granite, Brass &amp; Shingle</span>
    <span class="line-main">ROOFING</span>
  </h1>
</section>

<section class="card card--back">
  <div class="back-top">
    <div class="back-name">
      <span class="mark"></span>
      <div>
        <span class="line-top">Granite, Brass &amp; Shingle</span>
        <span class="line-main">ROOFING</span>
      </div>
    </div>
  </div>

  <div class="contact">
    <div class="person">Laszlo (Les) Varga</div>
    <div class="role">Owner</div>

    <div class="icon-row">
      <span class="rule"></span>
      <span class="icon" aria-label="Phone">
        <svg width="17" height="14" viewBox="0 0 17 14">
          <path d="M1 5 Q8.5 0 16 5 L14 7 L11.5 5.5 L11.5 4 Q8.5 3 5.5 4 L5.5 5.5 L3 7 Z" fill="#fff"/>
          <rect x="4" y="7" width="9" height="6" rx="1" fill="#fff"/>
        </svg>
      </span>
      <span class="icon" aria-label="Website">
        <svg width="17" height="17" viewBox="0 0 17 17">
          <circle cx="8.5" cy="8.5" r="7" fill="#fff"/>
          <path d="M5 4 Q7 5 6 7 Q8 9 6 12 M10 3 Q9 6 12 7 Q13 10 11 13" stroke="#000" stroke-width="1.6" fill="none"/>
        </svg>
      </span>
      <span class="icon" aria-label="Email">
        <svg width="17" height="13" viewBox="0 0 17 13">
          <rect x="1" y="1" width="15" height="11" fill="none" stroke="#fff" stroke-width="1.4"/>
          <path d="M1 1 L8.5 7.5 L16 1 M1 12 L6.5 6 M16 12 L10.5 6" stroke="#fff" stroke-width="1.2" fill="none"/>
        </svg>
      </span>
      <span class="rule"></span>
    </div>

    <div class="details">
      <div>(440)555-0187</div>
      <div class="web">www.granitebrassandshingleroofing.com</div>
      <div>gbsroofingllc@mail.com</div>
    </div>
    <div class="divider"></div>
    <div class="address">
      <div>2871 Millbrook Rd</div>
      <div>Fairview, OH 44093</div>
    </div>
  </div>
</section>

</body>
</html>
```